R. Korvane & Korvane----- Truck repair shop, specialized in Heavy Duty truck Engines and maintance

First of all, I am looking for the perfect logo. In other words, I want a simple and easy to remember. Nowadays, diesel engines have accomplished much technological progress in emission reductions. As a manager, I understand that technology is an important tool in this industry. I don't want the usual logo that I see in shops such as trucks, pistons, wrenches. I want a logo and then a phrase saying specialists in Diesel Engines.

Target Market(s)

Truck Drivers, logistic companies, fleet

Contact Information for Business Card

Simple. Easy logo to remember.

Font styles to use
Serif

Colors

Designer to choose colors to be used in the design.

Requirements
Must have
• Business name
• Address 482 Marlow Avenue Newark 07105 NJ
• Phone number
• email: rkorvaneandkorvane@brinmail.com
Nice to have
• the Name should be " R. Korvane & Korvane " not R. Korvane AND Korvane
Should not have
• card should not have the usual logos of mechanic shops. e.g. cars, trucks, just a Logo

```html
<!DOCTYPE html>
<html lang="en">
<head>
<meta charset="utf-8">
<title>R. Korvane &amp; Korvane — Business Card</title>
<link rel="stylesheet" href="https://fonts.googleapis.com/css2?family=Montserrat:wght@800&family=Lato:wght@400;700&display=swap">
<style>
  :root {
    --bg: #e9e6e1;
    --card-white: #f2f2f2;
    --brand-red: #d0282e;
    --brand-red-dark: #a91f25;
    --ink: #141414;
    --ink-soft: #3a3a3a;
    --trace-gold: #c9a15a;
  }
  * { box-sizing: border-box; margin: 0; padding: 0; }
  html, body { width: 1200px; height: 800px; overflow: hidden; }
  body {
    background: var(--bg);
    position: relative;
    font-family: "Lato", sans-serif;
    color: var(--ink);
  }
  .card {
    position: absolute;
    top: 245px;
    width: 540px;
    height: 310px;
    background: var(--card-white);
    border-radius: 4px;
    box-shadow: 0 6px 18px rgba(0,0,0,.18);
    overflow: hidden;
  }
  .card--front { left: 40px; }
  .card--back { left: 620px; }

  .brand {
    position: absolute;
    display: flex;
    align-items: center;
    gap: 12px;
  }
  .brand__mark {
    width: 22px; height: 22px;
    background: var(--brand-red);
    flex: none;
  }
  .brand__name {
    font-family: "Montserrat", sans-serif;
    font-weight: 800;
    letter-spacing: .5px;
    line-height: 1;
    white-space: nowrap;
  }
  .tagline {
    position: absolute;
    background: var(--ink);
    color: #fff;
    font-family: "Montserrat", sans-serif;
    font-weight: 800;
    letter-spacing: 1px;
    white-space: nowrap;
    line-height: 1;
  }

  /* Front */
  .logo-frame {
    position: absolute;
    left: 70px; top: 40px;
    width: 240px; height: 105px;
    border: 2px solid var(--ink-soft);
    border-radius: 10px;
  }
  .card--front .brand { left: 90px; top: 165px; }
  .card--front .brand__name { font-size: 32px; color: var(--ink); }
  .card--front .tagline { left: 124px; top: 215px; font-size: 15px; padding: 5px 10px; }

  /* Back */
  .red-panel {
    position: absolute; inset: 0;
    background: var(--brand-red);
    clip-path: polygon(0 0, 58% 0, 44% 100%, 0 100%);
  }
  .circuit-area {
    position: absolute;
    left: 40px; bottom: 0;
    width: 190px; height: 90px;
    background: linear-gradient(180deg, rgba(201,161,90,.1) 0%, rgba(201,161,90,.45) 100%);
    clip-path: polygon(0 100%, 100% 0, 100% 100%);
  }
  .card--back .brand { left: 22px; top: 112px; gap: 8px; }
  .card--back .brand__mark { width: 16px; height: 16px; background: #fff; }
  .card--back .brand__name { font-size: 18px; color: #fff; }
  .card--back .tagline { left: 22px; top: 146px; font-size: 11px; padding: 4px 8px; }

  .contact {
    position: absolute;
    left: 320px; top: 48px;
    width: 210px;
  }
  .contact__name { font-size: 20px; font-weight: 400; color: var(--ink); }
  .contact__role { font-size: 13px; color: var(--ink-soft); margin-top: 2px; }
  .contact__rule { width: 150px; height: 2px; background: var(--brand-red); margin: 12px 0 16px; }
  .contact__list { list-style: none; }
  .contact__item {
    display: flex; align-items: flex-start; gap: 7px;
    font-size: 12px; line-height: 1.3; color: var(--ink);
    margin-bottom: 8px;
  }
  .contact__icon {
    width: 16px; height: 16px; flex: none;
    border-radius: 50%; background: var(--ink);
    display: flex; align-items: center; justify-content: center;
  }
  .contact__icon svg { width: 10px; height: 10px; }
</style>
</head>
<body>
  <section class="card card--front" aria-label="Business card front">
    <div class="logo-frame"></div>
    <div class="brand">
      <span class="brand__mark"></span>
      <span class="brand__name">R. Korvane &amp; Korvane</span>
    </div>
    <div class="tagline">Specialists In Diesel Engines</div>
  </section>

  <section class="card card--back" aria-label="Business card back">
    <div class="red-panel"></div>
    <div class="circuit-area" role="img" aria-label="Gold circuit-trace pattern"></div>
    <div class="brand">
      <span class="brand__mark"></span>
      <span class="brand__name">R. Korvane &amp; Korvane</span>
    </div>
    <div class="tagline">Specialists In Diesel Engines</div>

    <div class="contact">
      <p class="contact__name">Marco Velandri</p>
      <p class="contact__role">Manager/Owner</p>
      <div class="contact__rule"></div>
      <ul class="contact__list">
        <li class="contact__item">
          <span class="contact__icon"><svg viewBox="0 0 10 10"><path d="M2 1.5h2l.6 2-1 .8a5 5 0 0 0 2.1 2.1l.8-1 2 .6v2c0 .5-.4.8-.9.8A7 7 0 0 1 1.2 2.4c0-.5.3-.9.8-.9z" fill="#fff"/></svg></span>
          <span>908-555-0172</span>
        </li>
        <li class="contact__item">
          <span class="contact__icon"><svg viewBox="0 0 10 10"><rect x="1.5" y="2.5" width="7" height="5" fill="none" stroke="#fff" stroke-width="1"/><path d="M1.5 2.5 5 5.5l3.5-3" fill="none" stroke="#fff" stroke-width="1"/></svg></span>
          <span>rkorvaneandkorvane@brinmail.com</span>
        </li>
        <li class="contact__item">
          <span class="contact__icon"><svg viewBox="0 0 10 10"><path d="M5 1a3 3 0 0 1 3 3c0 2-3 5-3 5S2 6 2 4a3 3 0 0 1 3-3z" fill="#fff"/><circle cx="5" cy="4" r="1" fill="#141414"/></svg></span>
          <span>482 Marlow Avenue<br>Newark NJ 07105</span>
        </li>
      </ul>
    </div>
  </section>
</body>
</html>
```